Dential Clinic Business Card

We need a simple elegant business card. 2 sided. First side with our details, and 2nd side with appointment time rows.

Dark background preferred. Will consider monotone design, or colored. Surprise us.

Details:
SIDE1

Maplewood Square Dental

Dr Peter Hollis
BDSc(Adel) FRZPTA

Shop 42, Maplewood Square
7-19 Birch Parade, Croydon VIC 3136
Phone: 03 9555 0148
email: info@maplewoodsquaredental.com.au
site: www.maplewoodsquaredental.com.au
_____________________________________
SIDE 2
Appointed Time ________________________
Notes _______________________

Target Market(s)

Dental Patients

Industry/Entity Type

Healthcare

Contact Information for Business Card

SIDE1

Maplewood Square Dental

Dr Peter Hollis
Shop 42, Maplewood Square
Phone: 03 9555 0148
SIDE 2

Font styles to use
Other font styles liked:
• Comfortaa

Requirements
Must have
• Dr Peter Hollis
BDSc(Adel) FRZPTA

Address
Phone
Email
Website
Nice to have
• Simple elegant design with our logo.
Colored logo.
Light text on dark background - Side 1
Light background so can be written on with dark pen - SIde 2
Should not have
• Too many colors

```html
<!DOCTYPE html>
<html lang="en">
<head>
<meta charset="utf-8">
<title>Maplewood Square Dental – Business Card</title>
<link rel="stylesheet" href="https://fonts.googleapis.com/css2?family=Roboto:wght@400;700&display=swap">
<style>
  :root {
    --blue: #1e96d4;
    --green: #7dbf45;
    --grey: #8a8b8d;
    --text-grey: #6f6f71;
    --white: #ffffff;
    --backdrop: #d9d9d9;
  }
  * { margin: 0; padding: 0; box-sizing: border-box; }
  html, body {
    width: 1125px; height: 1200px; overflow: hidden;
    background: var(--backdrop);
    font-family: "Roboto", Arial, sans-serif;
  }
  .canvas { position: relative; width: 1125px; height: 1200px; }
  .card {
    position: absolute; left: 151px; width: 826px; height: 472px;
    border-radius: 22px; overflow: hidden;
    box-shadow: 0 3px 6px rgba(0,0,0,0.25);
  }
  .card-front { top: 98px; background: var(--white); }
  .card-back { top: 631px; background: var(--blue); }
  .card-art { position: absolute; inset: 0; width: 100%; height: 100%; }
  .abs { position: absolute; }

  /* front */
  .doctor-name { left: 66px; top: 264px; font-size: 30px; font-weight: 700; color: var(--green); line-height: 1; }
  .doctor-creds { left: 66px; top: 301px; font-size: 20px; color: var(--text-grey); line-height: 1; }
  .contact-row { left: 66px; display: flex; align-items: center; gap: 12px; font-size: 21px; color: var(--text-grey); line-height: 1; }
  .contact-row svg { width: 20px; height: 20px; flex: none; }
  .contact-phone { top: 350px; }
  .contact-email { top: 383px; }
  .contact-web { top: 416px; }
  .accent { color: var(--blue); }
  .address { right: 61px; top: 360px; text-align: right; font-size: 21px; line-height: 28px; color: var(--text-grey); font-style: normal; }
  .brand-front { right: 61px; top: 118px; display: flex; flex-direction: column; align-items: center; gap: 16px; }
  .brand-mark { border-radius: 50%; }
  .brand-front .brand-mark { width: 70px; height: 70px; background: var(--blue); }
  .brand-front .brand-name { font-size: 29px; color: var(--blue); white-space: nowrap; }

  /* back */
  .brand-back { left: 40px; top: 42px; width: 260px; display: flex; flex-direction: column; align-items: center; gap: 12px; }
  .brand-back .brand-mark { width: 58px; height: 58px; background: var(--white); }
  .brand-back .brand-name { font-size: 21px; color: var(--white); white-space: nowrap; }
  .appointment-title { right: 55px; top: 68px; font-size: 21px; font-weight: 700; color: var(--white); }
  .divider { left: 0; right: 0; top: 171px; height: 2px; background: rgba(255,255,255,0.8); }
  .field-label { font-size: 21px; color: var(--white); line-height: 1; }
  .label-time { left: 54px; top: 211px; }
  .label-date { left: 416px; top: 211px; }
  .label-notes { left: 54px; top: 302px; }
  .field-box { background: var(--white); box-shadow: inset 0 1px 3px rgba(0,0,0,0.3); }
  .box-time { left: 52px; top: 243px; width: 345px; height: 42px; }
  .box-date { left: 416px; top: 243px; width: 356px; height: 42px; }
  .box-notes { left: 52px; top: 331px; width: 720px; height: 42px; }
  .back-url { left: 0; right: 0; top: 433px; text-align: center; font-size: 21px; color: var(--white); line-height: 1; }
</style>
</head>
<body>
<main class="canvas">

  <section class="card card-front" aria-label="Business card front">
    <svg class="card-art" viewBox="0 0 826 472" preserveAspectRatio="none" aria-hidden="true">
      <path d="M0 0 H238 C205 150 110 245 0 315 Z" fill="var(--blue)"/>
      <path d="M205 0 H770 C580 12 345 65 218 150 C232 100 230 45 205 0 Z" fill="var(--green)"/>
      <path d="M580 42 C690 8 780 0 808 6 L826 20 V125 C790 88 700 48 580 42 Z" fill="var(--grey)"/>
    </svg>

    <div class="abs brand-front">
      <span class="brand-mark"></span>
      <span class="brand-name">Maplewood Square Dental</span>
    </div>

    <h1 class="abs doctor-name">Dr Peter Hollis</h1>
    <p class="abs doctor-creds">BDSc(Adel) FRZPTA</p>

    <p class="abs contact-row contact-phone">
      <svg viewBox="0 0 24 24"><path fill="var(--green)" d="M6.6 10.8a15 15 0 0 0 6.6 6.6l2.2-2.2a1 1 0 0 1 1-.25 11.4 11.4 0 0 0 3.6.57 1 1 0 0 1 1 1V20a1 1 0 0 1-1 1A17 17 0 0 1 3 4a1 1 0 0 1 1-1h3.5a1 1 0 0 1 1 1c0 1.25.2 2.45.57 3.57a1 1 0 0 1-.25 1z"/></svg>
      <span>03 9555 0148</span>
    </p>
    <p class="abs contact-row contact-email">
      <svg viewBox="0 0 24 24"><rect x="3" y="6" width="18" height="12" rx="1.5" fill="none" stroke="var(--green)" stroke-width="2"/><path d="M3.5 7 12 13l8.5-6" fill="none" stroke="var(--green)" stroke-width="2"/></svg>
      <span>info@maplewoodsquaredental.com.au</span>
    </p>
    <p class="abs contact-row contact-web">
      <svg viewBox="0 0 24 24"><g fill="none" stroke="var(--green)" stroke-width="1.8"><circle cx="12" cy="12" r="9"/><ellipse cx="12" cy="12" rx="4" ry="9"/><path d="M3 12h18M5 7h14M5 17h14"/></g></svg>
      <span>www.<span class="accent">maplewoodsquaredental</span>.com.au</span>
    </p>

    <address class="abs address">
      Shop 42, Maplewood Square<br>
      7-19 Birch Parade<br>
      Elmsbury VIC 3999
    </address>
  </section>

  <section class="card card-back" aria-label="Business card back">
    <svg class="card-art" viewBox="0 0 826 472" preserveAspectRatio="none" aria-hidden="true">
      <path d="M0 438 H190 C196 424 202 419 215 419 H611 C624 419 630 424 636 438 H826 V472 H0 Z" fill="var(--green)" stroke="var(--white)" stroke-width="2"/>
    </svg>

    <div class="abs brand-back">
      <span class="brand-mark"></span>
      <span class="brand-name">Maplewood Square Dental</span>
    </div>
    <h2 class="abs appointment-title">Appointment</h2>
    <div class="abs divider"></div>

    <span class="abs field-label label-time">Time</span>
    <span class="abs field-label label-date">DATE</span>
    <div class="abs field-box box-time"></div>
    <div class="abs field-box box-date"></div>
    <span class="abs field-label label-notes">Notes</span>
    <div class="abs field-box box-notes"></div>

    <p class="abs back-url">www.maplewoodsquaredental.com.au</p>
  </section>

</main>
</body>
</html>
```